MARLOW CREST WINE LABEL DESIGN PROJECT

We need an elegant wine label design for our new range of wine. We need 3 labels for the range

2015 MARLOW CREST SHIRAZ
2015 MARLOW CREST CABERNET SAUVIGNON
2015 MARLOW CREST CABERNET SHIRAZ

The Size is nominated at 120mm High x 90mm Wide (Front and Back) but we are open to creative expression even if size differs

We are open to any style of label and designer can work on their strengths. it can be modern/classic/old fashion etc

I have attached the marlow crest logo ( the 2 olives) and a set up called wine mandatories which is in no way a design direction just the mandatory info that needs to appear on labels. The wine mandatories is just the information that needs to go on the label it has nothing to do with the design. DO not make designs based on this at all. These labels are for red wine not olive oil.

I have also attached some of the companies current olive oil labels ( TORQUALE AND WANDELLA AND MARLOW CREST so you can see other labels and how this wine product will sit in gift baskets.

Thanks
Tomasz.

Reason: Hello Friends We have decided to extend the deadline to enable more submissions. Many of the designs submitted have images of olives and look like olive oil product. We only need the olive logo to be shown on the label but the rest of the design should be a classic simple red wine label. It is not olive oil or olive product - it is red wine. Please keep simple and stylish Thanks Tomasz

Target Market(s)

35-65

Font styles to use
Serif

Requirements
Must have
• AS per brief
Nice to have
• as per brief
Should not have
• as per brief

```html
<!DOCTYPE html>
<html lang="en">
<head>
<meta charset="utf-8">
<title>Marlow Crest Wine Labels – Shiraz &amp; Cabernet Sauvignon 2015</title>
<link rel="stylesheet" href="https://fonts.googleapis.com/css2?family=Cinzel:wght@400;600&family=Sorts+Mill+Goudy:ital@0;1&display=swap">
<style>
  :root {
    --backdrop: #1f1f24;
    --frame-rose: #9e4f5c;
    --frame-rose-dark: #874150;
    --parchment-light: #f4ecdc;
    --parchment-mid: #ece0c8;
    --parchment-edge: #ddcbaa;
    --ink: #2a2522;
    --ink-soft: #4a423c;
    --olive-dark: #3b2a3f;
    --grape-deep: #3c3a6a;
    --grape-mid: #5d5a8c;
    --vine-green: #6f8f45;
    --vine-earth: #8e7a5c;
  }
  * { box-sizing: border-box; margin: 0; padding: 0; }
  html, body {
    width: 1200px; height: 800px; overflow: hidden;
    background: var(--backdrop);
  }
  .label-sheet {
    width: 1200px; height: 800px;
    display: flex; align-items: center; justify-content: center;
    gap: 26px;
  }
  .label {
    position: relative;
    width: 260px; height: 350px;
    border: 15px solid var(--frame-rose);
    outline: 1px solid var(--frame-rose-dark);
    outline-offset: -15px;
    background: radial-gradient(ellipse at 45% 40%, var(--parchment-light) 0%, var(--parchment-mid) 70%, var(--parchment-edge) 100%);
    font-family: "Sorts Mill Goudy", Georgia, serif;
    color: var(--ink);
    overflow: hidden;
  }
  .label-frame-band { position: absolute; inset: -15px; pointer-events: none; }

  /* brand mark */
  .brand { display: flex; align-items: center; gap: 6px; }
  .brand-dot {
    width: 18px; height: 18px; border-radius: 50%;
    background: var(--olive-dark); flex: none;
  }
  .brand-name {
    font-family: "Cinzel", Georgia, serif;
    font-weight: 400; font-size: 11px; letter-spacing: 2px;
    color: var(--ink);
  }

  /* front label */
  .front .brand { position: absolute; top: 26px; left: 22px; }
  .front .tagline {
    position: absolute; top: 52px; left: 22px;
    font-style: italic; font-size: 12px; color: var(--ink-soft);
  }
  .front .varietal {
    position: absolute; top: 82px; left: 22px; right: 22px;
    font-family: "Cinzel", Georgia, serif; font-weight: 400;
    font-size: 28px; line-height: 1.05; letter-spacing: 1px;
  }
  .front .varietal.long { font-size: 22px; }
  .front .vintage {
    position: absolute; left: 22px;
    font-size: 20px; letter-spacing: 2px;
  }
  .front .volume {
    position: absolute; top: 30px; right: 6px;
    writing-mode: vertical-rl; font-size: 9px; letter-spacing: 1px;
  }
  .front .alcohol {
    position: absolute; bottom: 18px; left: 4px;
    writing-mode: vertical-rl; transform: rotate(180deg);
    font-size: 9px; letter-spacing: 1px;
  }
  .vineyard-photo {
    position: absolute; right: 0; bottom: 0;
    width: 170px; height: 150px;
    border-top-left-radius: 150px 130px;
    background: radial-gradient(circle at 60% 55%, var(--grape-mid) 0%, var(--grape-deep) 35%, var(--vine-green) 65%, var(--vine-earth) 100%);
  }

  /* back label */
  .back .brand { position: absolute; top: 18px; left: 18px; }
  .back .brand-dot { width: 12px; height: 12px; }
  .back .brand-name { font-size: 9px; letter-spacing: 1.5px; }
  .back .back-title {
    position: absolute; top: 40px; left: 18px; right: 18px;
    font-family: "Cinzel", Georgia, serif; font-size: 11px; letter-spacing: 1px;
  }
  .back .tasting-note {
    position: absolute; top: 62px; left: 18px; width: 200px;
    font-size: 9.5px; line-height: 1.4; color: var(--ink-soft);
  }
  .back .code-box {
    position: absolute; right: 18px; bottom: 92px;
    width: 78px; height: 62px; border: 1px solid var(--ink);
  }
  .back .mandatories {
    position: absolute; left: 18px; bottom: 16px; width: 120px;
    font-size: 8px; line-height: 1.4; letter-spacing: 0.3px;
    text-transform: uppercase; color: var(--ink-soft);
  }
  .back .mandatories .alc-vol { margin-top: 4px; color: var(--ink); }
  .back .volume {
    position: absolute; right: 18px; bottom: 16px;
    font-size: 9px; letter-spacing: 1px;
  }
</style>
</head>
<body>
<main class="label-sheet">

  <!-- Shiraz front -->
  <article class="label front shiraz-front">
    <div class="label-frame-band" role="img" aria-label="Ornamental vine-pattern border in dusty rose"></div>
    <div class="brand"><span class="brand-dot"></span><span class="brand-name">THE MARLOW CREST</span></div>
    <p class="tagline">Premium Australian Wine</p>
    <h2 class="varietal">SHIRAZ</h2>
    <p class="vintage" style="top:118px">2015</p>
    <p class="volume">750 ml</p>
    <p class="alcohol">14.5% ALC/VOL</p>
    <div class="vineyard-photo" role="img" aria-label="Photograph of ripe Shiraz grape bunches on the vine"></div>
  </article>

  <!-- Shiraz back -->
  <article class="label back shiraz-back">
    <div class="label-frame-band" role="img" aria-label="Ornamental vine-pattern border in dusty rose"></div>
    <div class="brand"><span class="brand-dot"></span><span class="brand-name">THE MARLOW CREST</span></div>
    <h3 class="back-title">SHIRAZ 2015</h3>
    <p class="tasting-note">Deep crimson in the glass, this Shiraz opens with ripe plum, blackberry and a touch of pepper. Soft tannins and gentle oak lead to a long, warm finish. Enjoy with roast lamb or aged cheese.</p>
    <div class="code-box"></div>
    <div class="mandatories">
      <p>Produced by Marlow Crest Wine Company</p>
      <p>18 Vale Road, Elmgrove SA 5190</p>
      <p>Product of Australia</p>
      <p>Contains sulphites</p>
      <p>8.6 standard drinks</p>
      <p class="alc-vol">14.5% ALC/VOL</p>
    </div>
    <p class="volume">750 ml</p>
  </article>

  <!-- Cabernet Sauvignon front -->
  <article class="label front cabernet-front">
    <div class="label-frame-band" role="img" aria-label="Ornamental vine-pattern border in dusty rose"></div>
    <div class="brand"><span class="brand-dot"></span><span class="brand-name">THE MARLOW CREST</span></div>
    <p class="tagline">Premium Australian Wine</p>
    <h2 class="varietal long">CABERNET<br>SAUVIGNON</h2>
    <p class="vintage" style="top:134px">2015</p>
    <p class="volume">750 ml</p>
    <p class="alcohol">14.5% ALC/VOL</p>
    <div class="vineyard-photo" role="img" aria-label="Photograph of Cabernet Sauvignon grape bunches among vine leaves"></div>
  </article>

  <!-- Cabernet Sauvignon back -->
  <article class="label back cabernet-back">
    <div class="label-frame-band" role="img" aria-label="Ornamental vine-pattern border in dusty rose"></div>
    <div class="brand"><span class="brand-dot"></span><span class="brand-name">THE MARLOW CREST</span></div>
    <h3 class="back-title">CABERNET SAUVIGNON 2015</h3>
    <p class="tasting-note">Rich and elegant, this Cabernet Sauvignon shows blackcurrant, cedar and dark chocolate. Firm tannins and fine structure give a lingering finish. Pair with grilled beef or hearty pasta dishes.</p>
    <div class="code-box"></div>
    <div class="mandatories">
      <p>Produced by Marlow Crest Wine Company</p>
      <p>18 Vale Road, Elmgrove SA 5190</p>
      <p>Product of Australia</p>
      <p>Contains sulphites</p>
      <p>8.6 standard drinks</p>
      <p class="alc-vol">14.5% ALC/VOL</p>
    </div>
    <p class="volume">750 ml</p>
  </article>

</main>
</body>
</html>
```